Visitenkarten-Design für Immobilienmakler
Zielgruppe
Immobilienmakler
Aufgabenstellung
Top moderne hochwertige Visitenkate, wir hätten gerne eine sehr hochwertig moderne Visitenkarte mit Bild vom Mitarbeiter... Anbei habe ich die alte Visitenkarte die ich sehr kindlich finde... Es sollte jetzt sehr exklusive aussehen. Alle Daten können von der alten Visitenkarte übernommen werden.. danke

```html
<!DOCTYPE html>
<html lang="de">
<head>
<meta charset="utf-8">
<title>Falkner Agentur – Visitenkarte</title>
<link rel="stylesheet" href="https://fonts.googleapis.com/css2?family=Ubuntu:wght@400;500;700&display=swap">
<style>
  :root {
    --backdrop: #5b5c5e;
    --card: #ffffff;
    --brand-green: #1b8a44;
    --ink: #2b2b2b;
    --photo-light: #eef1f4;
    --photo-mid: #c9ced6;
  }
  * { margin: 0; padding: 0; box-sizing: border-box; }
  html, body {
    width: 1200px;
    height: 764px;
    overflow: hidden;
    background: var(--backdrop);
    font-family: "Ubuntu", sans-serif;
    color: var(--ink);
  }
  .stage { position: relative; width: 1200px; height: 764px; }
  .card {
    position: absolute;
    top: 290px;
    width: 488px;
    height: 316px;
    background: var(--card);
    box-shadow: 0 6px 16px rgba(0,0,0,0.35);
    overflow: hidden;
  }
  .card--front { left: 88px; }
  .card--back { left: 619px; }

  .wordmark {
    position: absolute;
    display: flex;
    align-items: center;
    gap: 8px;
    color: var(--brand-green);
    font-weight: 700;
    white-space: nowrap;
    letter-spacing: -0.5px;
  }
  .wordmark__dot {
    border-radius: 50%;
    background: var(--brand-green);
    flex: none;
  }
  .card--front .wordmark { left: 98px; top: 150px; font-size: 40px; }
  .card--front .wordmark__dot { width: 22px; height: 22px; }
  .card--back .wordmark { left: 194px; top: 38px; font-size: 26px; }
  .card--back .wordmark__dot { width: 14px; height: 14px; }

  .address {
    position: absolute;
    left: 194px;
    top: 88px;
    font-size: 13.5px;
    line-height: 18px;
    font-style: normal;
  }
  .contact {
    position: absolute;
    left: 194px;
    top: 131px;
    font-size: 13.5px;
    line-height: 17.5px;
    display: grid;
    grid-template-columns: 54px auto;
  }
  .name-band {
    position: absolute;
    left: 157px;
    right: 0;
    top: 212px;
    height: 29px;
    background: var(--brand-green);
    color: #fff;
    font-size: 18.5px;
    line-height: 29px;
    padding-left: 37px;
  }
  .role {
    position: absolute;
    left: 194px;
    top: 249px;
    font-size: 13.5px;
    line-height: 18px;
  }
  .portrait {
    position: absolute;
    left: 38px;
    top: 163px;
    width: 120px;
    height: 120px;
    border-radius: 50%;
    background: radial-gradient(circle at 50% 40%, var(--photo-light) 0%, var(--photo-mid) 100%);
    box-shadow: 0 2px 5px rgba(0,0,0,0.25);
  }
</style>
</head>
<body>
<main class="stage">
  <section class="card card--front" aria-label="Vorderseite">
    <div class="wordmark"><span>Falkner Agentur</span><span class="wordmark__dot"></span></div>
  </section>

  <section class="card card--back" aria-label="Rückseite">
    <div class="wordmark"><span>Falkner Agentur</span><span class="wordmark__dot"></span></div>
    <address class="address">Am Feldrain 12<br>6850 Talheim</address>
    <div class="contact">
      <span>Telefon</span><span>+43 5512 47 218 30</span>
      <span>Mobil</span><span>+43 660 4827 391</span>
      <span>Mail</span><span>lukas@falkner-agentur.com</span>
      <span>Web</span><span>www.falkner-agentur.com</span>
    </div>
    <div class="name-band">Lukas Berger</div>
    <div class="role">Dipl. Immobilienmanager<br>Geschäftsführer</div>
    <div class="portrait" role="img" aria-label="Porträtfoto des Mitarbeiters im weißen Hemd"></div>
  </section>
</main>
</body>
</html>
```